Web SITE design for new book

I need a unique design for a book my friend is releasing.

The home page needs to include:
A picture of the book
A spot for a video

Navigation:
Home
About the Book
Buy the Book
About the Author
Investing
Log In

The person awarded the project will also need to provide designs for the 5 other internal pages. They should be pretty straight forward.

Link to book design: https://www.filvantra.net/s/qmrt82kw7zpalvq/book-cover.png

Thanks!

```html
<!DOCTYPE html>
<html lang="en">
<head>
<meta charset="utf-8">
<title>The Pagefold — Home</title>
<link rel="stylesheet" href="https://fonts.googleapis.com/css2?family=Open+Sans:wght@300;400;600;700&family=Oswald:wght@500&display=swap">
<style>
:root{
  --ink:#222222;
  --gold:#b1954a;
  --gold-text:#9a7e3b;
  --body-text:#6b6b6b;
  --page:#ffffff;
  --panel-line:#d6d6d6;
  --footer-text:#e6e6e6;
  --video-blue:#13a3e6;
}
*{box-sizing:border-box;margin:0;padding:0}
html,body{width:1023px;height:1200px;overflow:hidden;background:var(--page);font-family:"Open Sans",Arial,sans-serif}
.site{position:relative;width:1023px;height:1200px}

/* header */
.site-header{position:absolute;left:0;top:0;width:1023px;height:98px;background:var(--ink);border-bottom:5px solid var(--gold)}
.login-button{position:absolute;left:815px;top:15px;width:67px;height:24px;background:var(--gold);border-radius:3px;color:#fff;font-weight:700;font-size:11.5px;line-height:24px;text-align:center;letter-spacing:.3px}
.brand{position:absolute;left:110px;top:50px;color:#fff;font-family:"Oswald",Arial,sans-serif;font-weight:500;font-size:26px;line-height:1;letter-spacing:-.3px}
.main-nav{position:absolute;top:59px;left:0;width:1023px;height:20px}
.main-nav a{position:absolute;color:#fff;text-decoration:none;font-size:14.5px;font-weight:400;line-height:20px;white-space:nowrap}
.main-nav .current-marker{position:absolute;left:318px;top:26px;width:0;height:0;border-left:6px solid transparent;border-right:6px solid transparent;border-bottom:8px solid var(--gold)}

/* hero slider */
.hero{position:absolute;left:133px;top:129px;width:757px;height:347px;border:1px solid var(--panel-line);background:linear-gradient(180deg,#f3f3f3,#e4e4e4)}
.hero-book{position:absolute;left:36px;top:18px;width:222px;height:315px;background:linear-gradient(100deg,#ffffff 0%,#eeeeee 70%,#2b2b2b 92%,#1a1a1a 100%);box-shadow:-8px 14px 18px rgba(0,0,0,.18)}
.hero-title{position:absolute;left:289px;top:89px;width:430px;color:var(--gold-text);font-weight:400;font-size:18.3px;line-height:25px}
.hero-copy{position:absolute;left:289px;top:158px;width:414px;color:var(--body-text);font-size:10.6px;line-height:19px}
.slider-dots{position:absolute;left:665px;top:311px;display:flex;gap:4.5px}
.slider-dots span{width:14px;height:14px;border-radius:50%;background:#111}
.slider-dots span.active{background:var(--gold)}

/* welcome */
.section-title{position:absolute;left:0;width:1023px;text-align:center;color:var(--gold-text);font-weight:400;font-size:19px;line-height:24px}
.welcome-title{top:506px}
.welcome-copy{position:absolute;left:146px;top:554px;width:732px;text-align:center;color:var(--body-text);font-size:10.6px;line-height:19px}
.videos-title{top:705px}

/* video */
.video{position:absolute;left:205px;top:750px;width:613px;height:344px;background:linear-gradient(180deg,#5f8f9a 0%,#b7c6c1 45%,#d9d3c4 62%,#cfc6b3 100%)}
.play-button{position:absolute;left:265px;top:135px;width:92px;height:56px;border-radius:5px;background:rgba(45,45,45,.88)}
.video-controls{position:absolute;left:72px;top:294px;width:478px;height:32px;border-radius:4px;background:rgba(50,55,58,.9)}

/* footer */
.site-footer{position:absolute;left:0;top:1126px;width:1023px;height:74px;background:var(--ink)}
.footer-nav{position:absolute;left:204px;top:13px;color:var(--footer-text);font-size:10.6px;line-height:16px;white-space:nowrap}
.footer-nav a{color:var(--footer-text);text-decoration:none}
.footer-nav .sep{margin:0 12px}
.copyright{position:absolute;left:204px;top:37px;color:var(--footer-text);font-size:10.6px;line-height:16px}
.social{position:absolute;left:792px;top:26px;display:flex;gap:8px}
.social span{width:18px;height:18px;border-radius:3px;background:#f2f2f2}
</style>
</head>
<body>
<div class="site">
  <header class="site-header">
    <div class="login-button">LOGIN</div>
    <div class="brand">THE PAGEFOLD</div>
    <nav class="main-nav">
      <a style="left:306px">HOME</a>
      <a style="left:377px">ABOUT THE BOOK</a>
      <a style="left:523px">BUY THE BOOK</a>
      <a style="left:650px">ABOUT THE AUTHOR</a>
      <a style="left:814px">INVESTING</a>
      <span class="current-marker"></span>
    </nav>
  </header>

  <section class="hero">
    <div class="hero-book" role="img" aria-label="3D render of the featured book with its white and gold cover"></div>
    <h2 class="hero-title">Sed ut perspiciatis unde omnis iste natus error sit voluptatem accusantium</h2>
    <p class="hero-copy">Eaque ipsa quae ab illo inventore veritatis et quasi architecto beatae vitae dicta sunt explicabo. Nemo enim ipsam voluptatem quia voluptas sit aspernatur aut odit aut fugit, sed quia consequuntur magni dolores eos qui ratione voluptatem sequi nesciunt. Sed ut perspiciatis unde omnis iste natus error sit voluptatem accusantium doloremque laudantium, totam rem aperiam</p>
    <div class="slider-dots"><span class="active"></span><span></span><span></span><span></span></div>
  </section>

  <h2 class="section-title welcome-title">WELCOME TO&nbsp; OUR BOOK WEBSITE</h2>
  <p class="welcome-copy">Sed ut perspiciatis unde omnis iste natus error sit voluptatem accusantium doloremque laudantium, totam rem aperiam, eaque ipsa quae ab illo inventore veritatis et quasi architecto beatae vitae dicta sunt explicabo. Nemo enim ipsam voluptatem quia voluptas sit aspernatur aut odit aut fugit, sed quia consequuntur magni dolores eos qui ratione voluptatem sequi nesciunt. Sed ut perspiciatis unde omnis iste natus error sit voluptatem accusantium doloremque laudantium, totam rem aperiam, eaque ipsa quae ab illo inventore veritatis et quasi architecto beatae vitae dicta sunt explicabo. Nemo enim ipsam voluptatem quia voluptas sit aspernatur aut odit aut fugit, sed quia consequuntur magni dolores eos qui ratione voluptatem sequi nesciunt.</p>

  <h2 class="section-title videos-title">FEATURED VIDEOS</h2>
  <div class="video" role="img" aria-label="Video still: business people in a desert lifting a rising red growth arrow">
    <div class="play-button">
      <svg width="92" height="56" viewBox="0 0 92 56"><path d="M37 15 L60 28 L37 41 Z" fill="#fff"/></svg>
    </div>
    <div class="video-controls">
      <svg width="478" height="32" viewBox="0 0 478 32">
        <rect x="9" y="9" width="440" height="14" fill="none" stroke="#9aa3a8" stroke-width="1"/>
        <rect x="11" y="11" width="347" height="10" fill="#6f777b"/>
        <rect x="11" y="11" width="125" height="10" fill="var(--video-blue)"/>
        <g fill="var(--video-blue)">
          <rect x="370" y="9" width="2.5" height="14"/><rect x="376" y="9" width="2.5" height="14"/><rect x="382" y="9" width="2.5" height="14"/>
          <rect x="388" y="9" width="2.5" height="14"/><rect x="394" y="9" width="2.5" height="14"/><rect x="400" y="9" width="2.5" height="14"/>
          <rect x="406" y="9" width="2.5" height="14"/>
        </g>
        <text x="415" y="22" fill="var(--video-blue)" font-family="Open Sans, Arial, sans-serif" font-weight="700" font-style="italic" font-size="15">HD</text>
        <g stroke="#fff" stroke-width="2" fill="none">
          <path d="M450 10 L455 15 M450 22 L455 17 M464 10 L459 15 M464 22 L459 17"/>
        </g>
      </svg>
    </div>
  </div>

  <footer class="site-footer">
    <div class="footer-nav"><a>HOME</a><span class="sep">|</span><a>ABOUT THE BOOK</a><span class="sep">|</span><a>BUY THE BOOK</a><span class="sep">|</span><a>ABOUT THE AUTHOR</a><span class="sep">|</span><a>INVESTING</a></div>
    <div class="copyright">© 2014 COMPANY NAME ,ALL RIGHTS RESERVED</div>
    <div class="social" aria-label="Social links"><span></span><span></span><span></span><span></span></div>
  </footer>
</div>
</body>
</html>
```